Restaurant Posters

Looking for two posters to be created for restaurant promos - see below for details:

Design #1 -
Want to highlight two main specials we offer - first is Tuesday BOGO Burgers (with purchase of two beverages), second is on Wednesday's we offer $0.75 Wings (includes traditional and boneless) and $2 off IPA's

Then at the bottom smaller would like to call out two less important offers - first is $2 off Nebraska Beers on Mondays, and the second is 1/2 off 19.2oz Crowlers on Thursdays

Design #2 -
Looking to create a sign up for our e-club and receive a free appetizer upon sign up, free burger on your birthday week, and access to exclusive deals and email offers

See attached for supporting docs you may use - don't have to but feel free to get creative with these. Would like the designs to be simple, and follow our brand look and feel as much as possible. Our website is not a good indication of our brand - I would go more off of our logos, and our menu design.

Need extra days to review

```html
<!DOCTYPE html>
<html lang="en">
<head>
<meta charset="utf-8">
<title>Prairie Tap House – Promo Posters</title>
<link rel="stylesheet" href="https://fonts.googleapis.com/css2?family=Bebas+Neue&family=Montserrat:wght@300;400;600;800&family=Mr+Dafoe&display=swap">
<style>
  :root{
    --wall:#eeeeee;
    --charcoal:#2d2d2d;
    --charcoal-deep:#1f1f1f;
    --red:#d71f30;
    --white:#ffffff;
    --ink:#1c1c1c;
    --grey-line:#6b6b6b;
  }
  *{margin:0;padding:0;box-sizing:border-box}
  html,body{width:1200px;height:800px;overflow:hidden}
  body{background:var(--wall);position:relative;font-family:"Montserrat",sans-serif}

  .poster{position:absolute;top:161px;width:368px;height:520px;overflow:hidden;
    background:radial-gradient(ellipse at 45% 35%, #4a4a4a 0%, var(--charcoal) 55%, var(--charcoal-deep) 100%);
    box-shadow:0 14px 28px rgba(0,0,0,.18)}
  .poster--specials{left:173px}
  .poster--eclub{left:660px}
  .poster > *{position:absolute}
  .backdrop{left:0;top:0;width:368px;height:520px}

  /* Specials poster */
  .brand-mark{top:30px;left:0;width:368px;display:flex;justify-content:center;align-items:center;gap:7px;
    font-family:"Bebas Neue",sans-serif;font-size:22px;color:var(--white);letter-spacing:1px}
  .brand-mark__dot{width:11px;height:11px;border-radius:50%;background:var(--white)}
  .day-script{top:66px;left:112px;z-index:3;font-family:"Mr Dafoe",cursive;font-size:60px;color:var(--white);line-height:1}
  .headline{top:114px;left:37px;z-index:2;font-family:"Bebas Neue",sans-serif;font-size:68px;line-height:1;color:var(--white);white-space:nowrap}
  .headline__accent{color:var(--red)}
  .offer-frame{left:0;top:0;width:368px;height:520px}
  .offer-condition{top:334px}
  .offer-sub{top:176px;left:0;width:368px;text-align:center;font-weight:600;font-size:13.6px;color:var(--white);letter-spacing:.2px}
  .deal{text-align:center;color:var(--white)}
  .deal__price{font-family:"Bebas Neue",sans-serif;font-size:36px;line-height:1}
  .deal__price sup{font-size:16px;vertical-align:top;position:relative;top:3px}
  .deal__off{font-size:24px}
  .deal__item{font-weight:300;font-size:19px;line-height:1}
  .deal__note{font-size:6px;margin-top:2px}
  .deal--wings{top:197px;left:84px;width:100px}
  .deal--ipa{top:197px;left:192px;width:100px}
  .deal--ipa .deal__item{font-size:22px;margin-top:2px}
  .deal-divider{left:190px;top:200px;width:1px;height:52px;background:var(--grey-line)}
  .food-photo{left:88px;top:272px;width:218px;height:190px;border-radius:48% 48% 30% 30%;
    background:radial-gradient(ellipse at 50% 45%, #f1dcc0 0%, #d98d3c 45%, #a65a22 80%, #6b3a1e 100%)}

  .minor-offers{top:476px;left:0;width:368px;height:34px}
  .minor{position:absolute;top:0;display:flex;align-items:flex-start;gap:6px}
  .minor__price{font-family:"Bebas Neue",sans-serif;font-size:22px;line-height:1;color:var(--ink)}
  .minor__price sup{font-size:11px;vertical-align:top}
  .minor__price small{font-size:14px}
  .minor__detail{font-size:8px;color:var(--ink);margin-top:1px}
  .minor__day{font-family:"Bebas Neue",sans-serif;font-size:14.5px;line-height:.98;color:var(--ink)}
  .minor__day span{color:var(--red);display:block}
  .minor--mon{left:68px}
  .minor--thu{left:198px}
  .minor-divider{position:absolute;left:179px;top:2px;width:1px;height:26px;background:var(--ink)}

  /* E-club poster */
  .signup{top:24px;left:31px;font-family:"Bebas Neue",sans-serif;font-size:70px;line-height:1;color:var(--red);white-space:nowrap}
  .signup__rest{font-family:"Montserrat",sans-serif;font-weight:800;font-size:25px;color:var(--white);margin-left:-2px}
  .receive{top:82px;left:34px;font-size:29px;font-weight:400;color:var(--white);letter-spacing:.5px}
  .reward{top:117px;left:32px;font-family:"Bebas Neue",sans-serif;font-size:52px;line-height:1;color:var(--white);letter-spacing:.5px}
  .perks{top:164px;left:33px;list-style:none}
  .perks li{display:flex;align-items:center;gap:9px;font-size:11px;color:var(--white);height:15px;letter-spacing:.2px}
  .perks svg{width:11px;height:11px;flex:none}
  .people-photo{left:0;top:193px;width:368px;height:282px;
    background:linear-gradient(90deg, #3a3a3a 0%, #b98fb4 25%, #c49a62 50%, #d7c0cf 72%, #3a3a3a 100%)}
  .footer-rule{left:0;top:475px;width:368px;height:6px;background:#4a4a4a}
  .footer{left:0;top:483px;width:368px;height:37px;background:var(--red);display:flex;align-items:center;padding:0 18px 0 34px;color:var(--white)}
  .footer__site{font-size:12.5px;letter-spacing:.3px}
  .footer__follow{margin-left:26px;font-size:6px;display:flex;align-items:center;gap:4px}
  .footer__follow i{width:8px;height:8px;background:var(--white);display:block}
  .footer__brand{margin-left:auto;font-family:"Bebas Neue",sans-serif;font-size:15px;line-height:.95;text-align:center;letter-spacing:.5px}
</style>
</head>
<body>

<section class="poster poster--specials">
  <svg class="backdrop" viewBox="0 0 368 520" aria-hidden="true">
    <polygon points="0,420 368,293 368,520 0,520" fill="#ffffff"/>
    <polygon points="0,388 368,235 368,263 0,420" fill="#d71f30"/>
    <line x1="190" y1="339" x2="368" y2="269" stroke="#ffffff" stroke-width="2.5"/>
    <rect x="0" y="511" width="325" height="9" fill="#2d2d2d"/>
    <polygon points="325,511 368,511 368,520 332,520" fill="#d71f30"/>
  </svg>

  <div class="brand-mark"><span class="brand-mark__dot"></span>Prairie Tap</div>
  <div class="day-script">Tuesday</div>
  <h1 class="headline">BOGO <span class="headline__accent">BURGERS</span></h1>

  <svg class="offer-frame" viewBox="0 0 368 520" aria-hidden="true">
    <path d="M52,182 H48 V241 H106" fill="none" stroke="#d71f30" stroke-width="1.2"/>
    <path d="M316,182 H320 V241 H276" fill="none" stroke="#d71f30" stroke-width="1.2"/>
    <circle cx="106" cy="241" r="2" fill="#d71f30"/>
    <circle cx="276" cy="241" r="2" fill="#d71f30"/>
  </svg>
  <p class="offer-sub">With Purchase of two beverages</p>

  <div class="deal deal--wings">
    <div class="deal__price"><sup>$</sup>0.75</div>
    <div class="deal__item">Wings</div>
    <div class="deal__note">Traditional and boneless</div>
  </div>
  <div class="deal-divider"></div>
  <div class="deal deal--ipa">
    <div class="deal__price"><sup>$</sup>2 <span class="deal__off">OFF</span></div>
    <div class="deal__item">IPA's</div>
  </div>

  <div class="food-photo" role="img" aria-label="Photo of a loaded burger with fried chicken, melted cheese and tater tots"></div>

  <div class="minor-offers">
    <div class="minor minor--mon">
      <div>
        <div class="minor__price"><sup>$</sup>2 <small>OFF</small></div>
        <div class="minor__detail">Nebraska</div>
      </div>
      <div class="minor__day">BEERS ON<span>MONDAYS</span></div>
    </div>
    <div class="minor-divider"></div>
    <div class="minor minor--thu">
      <div>
        <div class="minor__price">1/2 <small>OFF</small></div>
        <div class="minor__detail">19.2oz</div>
      </div>
      <div class="minor__day">CROWLERS ON<span>THURSDAYS</span></div>
    </div>
  </div>
</section>

<section class="poster poster--eclub">
  <h1 class="signup">SIGN UP<span class="signup__rest">our E-Club</span></h1>
  <p class="receive">And Receive</p>
  <p class="reward">A FREE APPETIZER</p>
  <ul class="perks">
    <li><svg viewBox="0 0 12 12"><circle cx="6" cy="6" r="5" fill="none" stroke="#d71f30" stroke-width="1"/><path d="M3.5,6 L5.4,7.8 L9.5,3.2" fill="none" stroke="#d71f30" stroke-width="1.1"/></svg>Free burger on your birthday week</li>
    <li><svg viewBox="0 0 12 12"><circle cx="6" cy="6" r="5" fill="none" stroke="#d71f30" stroke-width="1"/><path d="M3.5,6 L5.4,7.8 L9.5,3.2" fill="none" stroke="#d71f30" stroke-width="1.1"/></svg>Access to exclusive deals and email offers</li>
  </ul>
  <div class="people-photo" role="img" aria-label="Photo of two excited guests with a burger between them"></div>
  <div class="footer-rule"></div>
  <footer class="footer">
    <span class="footer__site">www.yourwebsite.com</span>
    <span class="footer__follow">Follow Us <i></i></span>
    <span class="footer__brand">PRAIRIE<br>TAP HOUSE</span>
  </footer>
</section>

</body>
</html>
```